Make it cool to work near where you are...

Calling all creatives - create the ultimate cool card for people who want to cut their commute.

Here at TilloPod we've got what can best be described as an Marlin pass for desks - and we want to brighten up the wallets of our most loyal users.

So, pitch us your ideas and you might see your design on cards being flashed across the country - and we've thrown in a bit of cash too.

Do see our brief card guidelines - with a couple of past examples thrown in.

Industry/Entity Type

Cash

```html
<!DOCTYPE html>
<html lang="en">
<head>
<meta charset="utf-8">
<title>TilloPod Card – work near, go far</title>
<link href="https://fonts.googleapis.com/css2?family=Arimo:wght@400;700&display=swap" rel="stylesheet">
<style>
  :root {
    --paper: #ffffff;
    --ink: #111111;
    --charcoal: #333333;
    --mist: #c9c9c9;
    --edge: #7a7a7a;
    --blush: #eecfcf;
    --banana: #f6c72a;
  }
  html, body {
    margin: 0;
    padding: 0;
    width: 1089px;
    height: 1200px;
    overflow: hidden;
    background: var(--paper);
    font-family: "Arimo", Arial, sans-serif;
  }
  .canvas {
    position: relative;
    width: 1089px;
    height: 1200px;
  }
  .card {
    position: absolute;
    left: 0;
    top: 0;
    width: 1087px;
    height: 598px;
    border: 1px solid var(--edge);
    background: var(--paper);
    overflow: hidden;
  }
  .card__wedge {
    position: absolute;
    left: 0;
    top: 0;
  }
  .card__tagline {
    position: absolute;
    left: 952px;
    top: 22px;
    font-size: 31px;
    color: var(--ink);
    margin: 0;
    line-height: 1;
  }
  .card__headline {
    position: absolute;
    left: 34px;
    top: 176px;
    margin: 0;
    font-weight: 400;
    font-size: 104px;
    line-height: 1;
    letter-spacing: -1px;
    color: var(--ink);
  }
  .card__headline .near {
    color: var(--mist);
  }
  .card__number {
    position: absolute;
    left: 142px;
    top: 345px;
    margin: 0;
    font-size: 42px;
    color: var(--ink);
    letter-spacing: 1px;
  }
  .card__band {
    position: absolute;
    left: 0;
    top: 455px;
    width: 100%;
    height: 143px;
    background: var(--charcoal);
  }
  .card__web {
    position: absolute;
    left: 0;
    width: 1040px;
    top: 508px;
    text-align: center;
    margin: 0;
    font-size: 34px;
    font-weight: 700;
    color: var(--paper);
  }
  .card__brand {
    position: absolute;
    left: 818px;
    top: 415px;
    width: 184px;
    height: 100px;
    border: 4px solid var(--paper);
    border-radius: 10px;
    background: var(--charcoal);
    color: var(--paper);
    font-weight: 700;
    font-size: 36px;
    display: flex;
    align-items: center;
    justify-content: center;
    box-sizing: border-box;
  }
  .fruit-photo {
    position: absolute;
    left: 0;
    top: 620px;
    width: 1089px;
    height: 580px;
    background:
      radial-gradient(ellipse 48% 22% at 50% 52%, var(--banana) 0%, var(--banana) 55%, rgba(246,199,42,0) 100%),
      var(--blush);
  }
</style>
</head>
<body>
<main class="canvas">
  <section class="card" aria-label="TilloPod membership card">
    <svg class="card__wedge" width="1087" height="455" viewBox="0 0 1087 455" aria-hidden="true">
      <polygon points="270,208 1058,43 1075,63 526,273" fill="var(--charcoal)"/>
    </svg>
    <p class="card__tagline">go far</p>
    <h1 class="card__headline">work <span class="near">near</span></h1>
    <p class="card__number">0047 316 205 418</p>
    <div class="card__band"></div>
    <div class="card__brand">TilloPod</div>
    <p class="card__web">www.tillopod.com</p>
  </section>
  <div class="fruit-photo" role="img" aria-label="Photo of a ripe yellow banana lying across a soft pink background"></div>
</main>
</body>
</html>
```